Poetry Book Cover Design Project

Looking for a minimalistic book cover design for a collection of poems. The book title is "Before The Morning Turns To Glass". There are three parts to the book. First covers poetry in the theme of Rage. Second love and desire. The third is strange poems. Essentially the sections are "Rage", "Desire" and the "Strange". The reason for the title "Before The Morning Turns To Glass" is as if someone is writing these till life changes towards the intended outcome as felt in each poem. I want to have the author's name "Nirosha Kulathunge" at the bottom. Ilustration attached.
- Minimalistic

```html
<!DOCTYPE html>
<html lang="en">
<head>
<meta charset="utf-8">
<title>Before The Morning Turns To Glass — Cover</title>
<link rel="stylesheet" href="https://fonts.googleapis.com/css2?family=Playfair+Display:wght@700;900&display=swap">
<style>
  :root {
    --page: #ffffff;
    --cover: #e9e9ea;
    --cover-light: #f3f3f4;
    --arc: #f7f7f7;
    --ring: #cfcfd2;
    --ink: #2a2a2a;
    --black: #111111;
    --blue-deep: #1d56a4;
    --blue: #3a7fbd;
    --orange: #f08a4b;
    --red: #e21f2b;
  }
  html, body {
    margin: 0;
    padding: 0;
    width: 1200px;
    height: 886px;
    overflow: hidden;
    background: var(--page);
  }
  .canvas {
    position: relative;
    width: 1200px;
    height: 886px;
  }
  .cover {
    position: absolute;
    left: 330px;
    top: 43px;
    width: 540px;
    height: 800px;
    background: linear-gradient(160deg, var(--cover-light), var(--cover));
    overflow: hidden;
    box-shadow: 0 2px 10px rgba(0,0,0,0.12);
  }
  .cover-art {
    position: absolute;
    inset: 0;
  }
  .title {
    position: absolute;
    right: 40px;
    top: 175px;
    margin: 0;
    text-align: right;
    font-family: "Playfair Display", Georgia, serif;
    font-weight: 900;
    font-size: 60px;
    line-height: 74px;
    letter-spacing: -0.5px;
  }
  .title span { display: block; }
  .title .w1 { color: var(--ink); }
  .title .w2 { color: var(--blue-deep); }
  .title .w3 { color: var(--orange); }
  .title .w4 { color: var(--blue); }
  .title .w5 { color: var(--red); }
  .title .w6 { color: var(--black); }
  .author {
    position: absolute;
    left: 62px;
    top: 676px;
    margin: 0;
    font-family: "Playfair Display", Georgia, serif;
    font-weight: 900;
    font-size: 17px;
    color: var(--black);
  }
</style>
</head>
<body>
<div class="canvas">
  <section class="cover">
    <svg class="cover-art" width="540" height="800" viewBox="0 0 540 800" aria-hidden="true">
      <g class="backdrop-arcs" fill="none" stroke="var(--arc)" stroke-width="14">
        <circle cx="-60" cy="900" r="420"/>
        <circle cx="-60" cy="900" r="500"/>
        <circle cx="-60" cy="900" r="580"/>
        <circle cx="-60" cy="900" r="660"/>
        <circle cx="-60" cy="900" r="740"/>
        <circle cx="-60" cy="900" r="820"/>
      </g>
      <g class="rings" fill="none" stroke="var(--ring)" stroke-width="2">
        <circle cx="110" cy="62" r="4"/>
        <circle cx="380" cy="125" r="4"/>
        <circle cx="200" cy="240" r="4"/>
        <circle cx="395" cy="250" r="6"/>
        <circle cx="355" cy="445" r="6"/>
        <circle cx="30" cy="500" r="4"/>
        <circle cx="150" cy="505" r="3"/>
        <circle cx="170" cy="585" r="7"/>
        <circle cx="55" cy="615" r="6"/>
      </g>
      <polygon class="corner-orange" points="410,0 540,0 540,150" fill="var(--orange)"/>
      <g class="hatch" stroke="var(--ink)" stroke-width="1.2" opacity="0.7">
        <line x1="372" y1="50" x2="380" y2="38"/>
        <line x1="380" y1="50" x2="388" y2="38"/>
        <line x1="388" y1="50" x2="396" y2="38"/>
        <line x1="396" y1="50" x2="404" y2="38"/>
        <line x1="404" y1="50" x2="412" y2="38"/>
        <line x1="412" y1="50" x2="420" y2="38"/>
        <line x1="420" y1="50" x2="428" y2="38"/>
        <line x1="428" y1="50" x2="436" y2="38"/>
        <line x1="436" y1="50" x2="444" y2="38"/>
      </g>
      <polygon class="shape-red" points="0,230 265,150 195,365 0,262" fill="var(--red)"/>
      <polygon class="shape-blue" points="0,295 178,388 0,470" fill="var(--blue)"/>
    </svg>
    <h1 class="title">
      <span class="w1">Before</span>
      <span class="w2">The</span>
      <span class="w3">Morning</span>
      <span class="w4">Turns</span>
      <span class="w5">To</span>
      <span class="w6">Glass</span>
    </h1>
    <p class="author">Nirosha Kulathunge</p>
  </section>
</div>
</body>
</html>
```